Refresh and update our Juice bottle label to a more vibrant and eye catching brand

We’ve had this label and included trademarked logo for the past 10 years. We do change the name of the juice ands its ingredients accordingly.
I want to up-date this round juice bottle label so it is more eye catching , trendy and clearly screams (healthy/juice/delicious/refreshing/beauty/youthful/high energy.
I have attached my trademarked logos as well as examples of a few labels. I also attached a few pictures of our juices with the current label which is a 2x4 inch front and back. I want you to see how colorful our juice is. I want the updated label to include out trademarked logo somehow but add in some color or graphics that speak to the message above in (). Open to adding color and even having a wrap around label instead of front and back=

Target Market(s)

Upscale women:men, age 20-65 40:30 ratio, health/ fitness/ body aware, anti aging/ high energy/ prevention of disease. Clientele is primarily caucasian.

Industry/Entity Type

Beverage, cold-pressed juice, wellness

Font styles to use
Sans Serif

Colors
59FF00
82FF00
B8FF75
E3FFCB
F4FFEA
EB3D1F
EC4F4E
F09395
F8D3D4
FCEDEE
E54698
E96AAD
F1A4CE
F9D9EA
FCEFF6
6B429C
8869AF
B7A5CE
E3DAEB
F3F0F8

Requirements
Must have
• My trademarked logo incorporated somehow. Bright/simple/modern/trendy style. I need to be able to change out the name of the juice and its ingredients and nutritional information. I want the label to say “100% Juice” basically this all needs to be on it: Name and Address. The name and address of your juicing business. ... Name of the Food. You should list the name of the food that is commonly used. ... What is the Amount of Juice inside of the bottle? ... % of juice declaration. ... Ingredients. ... Food Allergen (made in a facility with nuts). ... The Disclaimer. Must say “cold-pressed juice”
Nice to have
• Maybe a graphic image of a piece of fruit like a lemon with sliced cucumbers, I want vibrant colors added such as maybe use hot pink -outline or graphic on my Sip Tide Calm? since the juice is pink. Or a bright yellow on my Ran Bolt? Or a bright green on Vex Lumo. Maybe some wording like “no added sugar or preservatives”, “gluten free”
Should not have
• No health guarantees

```html
<!DOCTYPE html>
<html lang="en">
<head>
<meta charset="utf-8">
<title>Ran Bolt? – Juice Label, Front and Back</title>
<link rel="stylesheet" href="https://fonts.googleapis.com/css2?family=Montserrat:wght@500;600;700;800&family=Oswald:wght@500&family=Carlito:wght@400;700&display=swap">
<style>
  :root {
    --canvas: #ffffff;
    --label-bg: #f4ffea;
    --label-tint: #e3ffcb;
    --green-deep: #0b6a2f;
    --green-ink: #17602a;
    --lime: #82ff00;
    --lime-bright: #59ff00;
    --lime-soft: #b8ff75;
  }
  * { box-sizing: border-box; margin: 0; padding: 0; }
  html, body { width: 1200px; height: 848px; overflow: hidden; background: var(--canvas); }
  .canvas { position: relative; width: 1200px; height: 848px; }

  .label {
    position: absolute; top: 148px; width: 300px; height: 552px; overflow: hidden;
    background: var(--label-bg); color: var(--green-ink);
    display: flex; flex-direction: column; align-items: center;
    border-top: 6px solid var(--lime-bright);
    box-shadow: 0 2px 12px rgba(0,0,0,.12);
  }
  .label--front { left: 226px; }
  .label--back { left: 664px; }

  .brand {
    display: flex; align-items: center; gap: 10px; height: 48px;
    font-family: "Montserrat", sans-serif; font-weight: 700;
    color: var(--green-deep); font-size: 23px; line-height: 1.05;
  }
  .brand__dot { width: 28px; height: 28px; border-radius: 50%; background: var(--lime); flex: none; }
  .label--front .brand { margin-top: 38px; }
  .label--back .brand { margin-top: 38px; font-size: 21px; }

  .band { width: 100%; background: var(--green-deep); color: var(--lime); text-align: center; }
  .band--name {
    margin-top: 22px; height: 46px; line-height: 46px;
    font-family: "Montserrat", sans-serif; font-weight: 800; font-size: 24px; letter-spacing: .6px;
  }
  .band--shelf {
    margin-top: 34px; height: 52px; padding-top: 4px;
    font-family: "Oswald", sans-serif; font-weight: 500; font-size: 15px; line-height: 22px; letter-spacing: .6px;
  }

  .process-tag {
    margin-top: 12px;
    font-family: "Montserrat", sans-serif; font-weight: 700; font-size: 11px; letter-spacing: 2.4px;
    color: var(--green-deep); text-transform: uppercase;
  }

  .ingredients {
    list-style: none; margin-top: 12px; text-align: center;
    font-family: "Montserrat", sans-serif; font-weight: 600; font-size: 13px; line-height: 23px;
    text-transform: uppercase;
  }

  .claims { display: flex; gap: 6px; margin-top: 12px; }
  .claim {
    font-family: "Montserrat", sans-serif; font-weight: 700; font-size: 9.5px; letter-spacing: .4px;
    text-transform: uppercase; color: var(--green-deep);
    background: var(--label-tint); border: 1.5px solid var(--lime-bright);
    border-radius: 20px; padding: 4px 8px;
  }

  .fruit-photo {
    margin-top: auto; width: 100%; height: 176px;
    background: linear-gradient(160deg, var(--lime-soft) 0%, var(--lime) 55%, var(--lime-bright) 100%);
  }

  .facts {
    font-family: "Carlito", sans-serif; font-size: 11px; line-height: 14px;
    text-align: center; padding: 0 22px;
  }
  .facts--juice { margin-top: 18px; }
  .facts--warning { margin-top: 16px; }
  .facts--allergen { margin-top: 12px; }
  .facts--address { margin-top: 14px; }
  .facts--volume { margin-top: 14px; }
  .facts strong { font-weight: 700; }

  .site {
    margin-top: auto; margin-bottom: 22px;
    font-family: "Montserrat", sans-serif; font-weight: 700; font-size: 14px; color: var(--green-deep);
  }
  .label--back::after {
    content: ""; position: absolute; left: 0; bottom: 0; width: 100%; height: 8px;
    background: linear-gradient(90deg, var(--lime-bright), var(--lime-soft));
  }
</style>
</head>
<body>
<main class="canvas">

  <section class="label label--front" aria-label="Front label">
    <div class="brand"><span class="brand__dot"></span><span>Leafy<br>Pour?</span></div>
    <h1 class="band band--name">RAN BOLT?</h1>
    <p class="process-tag">Cold-Pressed Juice</p>
    <ul class="ingredients">
      <li>Pineapple</li>
      <li>Fuji Apple</li>
      <li>Lemon</li>
      <li>Turmeric Root</li>
    </ul>
    <div class="claims">
      <span class="claim">100% Juice</span>
      <span class="claim">No Added Sugar</span>
    </div>
    <div class="fruit-photo" role="img" aria-label="Close-up photo of thin cucumber slices"></div>
  </section>

  <section class="label label--back" aria-label="Back label">
    <div class="brand"><span class="brand__dot"></span><span>Leafy<br>Pour?</span></div>
    <p class="band band--shelf">BEST IF USED WITHIN 5 DAYS OF<br>PURCHASE</p>
    <p class="facts facts--juice">100% VEGETABLE &amp; FRUIT COLD-PRESSED JUICE. No added sugar or preservatives. Perishable, Keep Refrigerated. Shake Well *separation is natural*</p>
    <p class="facts facts--warning"><strong>WARNING:</strong> This product has not been pasteurized and, therefore may contain harmful bacteria that can cause serious illness in children, the elderly, and persons with weakened immune systems.</p>
    <p class="facts facts--allergen"><strong>ALLERGEN:</strong> Made in a facility that processes nuts.</p>
    <p class="facts facts--address">4180 Harbor Vale Rd #9, Cove Ridge, CA 90000</p>
    <p class="facts facts--volume">Net Wt. 12oz (354mL)</p>
    <p class="site">leafypour.com</p>
  </section>

</main>
</body>
</html>
```